"Landing Page Design for Premium Eco-Friendly Laundry Strips – Plooifris.nl"

We need a visually appealing and high-converting landing page for our premium laundry strips, emphasizing luxury, sustainability, and ease of use. The page should include sections such as:

Hero Section: A compelling introduction with a strong headline, subheadline, and a clear call-to-action (CTA).
Product Benefits: Highlighting key features like eco-friendliness, long-lasting scent, and hypoallergenic qualities.
Product Description: Focusing on innovation and sustainability.
How It Works: Simple, visual steps for using the product.
Customer Reviews: Authentic testimonials to build trust and social proof.
FAQ Section: Addressing common concerns about the product.
The design should maintain a luxurious aesthetic while ensuring clarity and user-friendliness. We also offer free shipping on all orders, a key differentiator to be prominently displayed. All texts and translations are already provided for implementation. Please deliver the design in Figma format."

Target Market(s)

"Eco-conscious consumers and families seeking premium and sustainable laundry solutions. Target age group: 25-50, predominantly women who prioritize luxury and environmental impact."

Industry/Entity Type

"Laundry care and eco-friendly consumer goods."

Coding

Requirements
Must have
• A visually luxurious design emphasizing premium quality and eco-friendliness. Clear call-to-actions (e.g., 'Try Now – Free Shipping'). Sections for product benefits, how it works, customer reviews, and FAQ. Highlight free shipping with no minimum order prominently."
Nice to have
• Elegant, minimalist animations to enhance the premium feel. Subtle use of gold and black to emphasize luxury, with a touch of green for sustainability. Interactive customer reviews section (e.g., carousel or testimonials)."
Should not have
• Overly cluttered designs or overwhelming text blocks. Generic stock photos not aligned with our brand identity. Bright or overly playful color schemes that detract from the premium feel."

```html
<!DOCTYPE html>
<html lang="en">
<head>
<meta charset="utf-8">
<title>Plooifris – Premium Laundry Strips</title>
<link href="https://fonts.googleapis.com/css2?family=Merriweather:wght@400;700;900&family=Roboto:wght@400;500;700&display=swap" rel="stylesheet">
<style>
:root{
  --gold:#c8952a;
  --gold-light:#e6bb45;
  --gold-dark:#a87a17;
  --ink:#1b1b1d;
  --ink-soft:#242427;
  --text:#333;
  --muted:#555;
  --line:#d9d9d9;
  --white:#fff;
  --serif:'Merriweather', Georgia, serif;
  --sans:'Roboto', Arial, sans-serif;
}
*{box-sizing:border-box;margin:0;padding:0}
html,body{width:1200px;height:4777px;overflow:hidden}
body{font-family:var(--sans);color:var(--text);background:var(--white);position:relative}
section,header,footer{position:relative;width:1200px;overflow:hidden}
.abs{position:absolute}
.gold-btn{background:linear-gradient(180deg,var(--gold-light),var(--gold-dark));color:#fff;font-weight:700;border-radius:3px;display:flex;align-items:center;justify-content:center}
.divider{position:absolute;left:50%;transform:translateX(-50%);width:142px;height:22px}
.section-title{position:absolute;left:0;width:1200px;text-align:center;font-family:var(--serif);font-weight:700}

/* top bar + nav */
.topbar{height:41px;background:var(--gold);color:#fff;font:700 14px var(--sans);display:flex;align-items:center;justify-content:center;letter-spacing:.2px}
.nav{height:70px;background:#fff;z-index:5;overflow:visible}
.brand{position:absolute;left:119px;top:-36px;width:150px;height:150px;border-radius:50%;background:#fff;display:flex;flex-direction:column;align-items:center;justify-content:center;z-index:6}
.brand .dot{width:54px;height:54px;border-radius:50%;background:var(--gold);margin-bottom:8px;margin-top:18px}
.brand .name{font:400 17px var(--serif);color:var(--gold)}
.nav-links{position:absolute;left:401px;top:26px;display:flex;font:400 13px var(--serif);color:#222;text-transform:uppercase}
.nav-links a{color:inherit;text-decoration:none;margin-right:46px}
.nav-links a.active{color:var(--gold)}

/* hero */
.hero{height:585px;background:linear-gradient(100deg,#2a2724 0%,#3b3733 45%,#6d6a66 75%,#4a4744 100%)}
.hero-photo{position:absolute;inset:0;background:radial-gradient(circle at 80% 45%,rgba(240,240,240,.35) 0,rgba(120,110,100,.2) 22%,rgba(0,0,0,0) 45%)}
.hero .kicker{left:111px;top:128px;font:700 34px var(--serif);color:var(--gold-light)}
.hero h1{left:111px;top:178px;width:490px;font:400 45px/52px var(--serif);color:#fff}
.hero .sub{left:111px;top:348px;font:700 17px var(--sans);color:#fff}
.hero .cta{left:111px;top:390px;width:134px;height:46px;font-size:16px}

/* benefits */
.benefits{height:686px;background:#fff}
.benefits .section-title{top:75px;font-size:30px;color:#111}
.benefit{position:absolute;width:316px;text-align:center}
.benefit .icon{margin:0 auto;width:160px;height:160px;position:relative}
.benefit h3{font:700 16px var(--serif);color:#111;margin-top:20px;letter-spacing:.4px}
.benefit p{font:400 14px/29px var(--sans);color:#444;margin:14px auto 0;width:262px}
.benefit.featured{background:#fff;border-radius:10px;box-shadow:0 6px 24px rgba(0,0,0,.14);border-bottom:6px solid var(--gold);height:384px;padding-top:24px}
.benefit .more{display:inline-flex;align-items:center;gap:8px;font:700 15px var(--sans);color:var(--gold);margin-top:14px;text-decoration:underline}

/* product */
.product{height:662px;background:radial-gradient(circle at 30% 60%,#3a3a3c 0,#222224 55%,#1b1b1d 100%)}
.product-art{left:195px;top:130px;width:284px;height:426px;border-radius:4px;background:linear-gradient(160deg,#4a4640 0%,#35322e 55%,#2a2826 100%)}
.product .eyebrow{left:633px;top:95px;font:700 30px var(--serif);color:var(--gold-light)}
.product .rule{left:633px;top:146px;width:58px;height:3px;background:var(--gold)}
.product .pname{left:633px;top:175px;font:700 22px var(--serif);color:#fff}
.product .price{left:633px;top:218px;font:700 23px var(--serif);color:var(--gold-light)}
.product .desc{left:633px;top:264px;width:440px;font:400 14.5px/31px var(--sans);color:#ddd}
.product .point{left:633px;width:440px;display:flex;gap:20px;font:400 14.5px/31px var(--sans);color:#ddd}
.product .cta{left:642px;top:514px;width:243px;height:45px;font:700 16px var(--serif);border-radius:2px}

/* how it works */
.how{height:761px;background:#fafafa}
.how .section-title{top:80px;font-size:31px;color:#111}
.how .intro{position:absolute;left:125px;top:188px;width:950px;text-align:center;font:400 14.5px/26px var(--sans);color:#333}
.step{position:absolute;width:216px;text-align:center}
.step .diamond{position:relative;width:216px;height:150px}
.step .diamond .sq{position:absolute;left:58px;top:25px;width:100px;height:100px;transform:rotate(45deg);background:linear-gradient(135deg,var(--gold-light),var(--gold-dark));border-radius:4px}
.step .badge{position:absolute;left:146px;top:-2px;width:76px;height:76px;border-radius:50%;background:#fff;border:2px solid var(--gold);font:700 13px/18px var(--sans);color:#222;display:flex;flex-direction:column;align-items:center;justify-content:center}
.step h3{font:700 17px var(--serif);color:#111;margin-top:12px}
.step p{font:400 14px/26px var(--sans);color:#444;margin-top:10px}

/* testimonials */
.testimonials{height:489px;background:var(--ink)}
.testimonials .section-title{top:70px;font-size:33px;color:var(--gold-light)}
.quote-mark{position:absolute;left:572px;top:193px;width:56px;height:56px;border-radius:50%;border:2px solid var(--gold);display:flex;align-items:center;justify-content:center;color:#fff;font:900 28px var(--serif)}
.testimonials blockquote{position:absolute;left:160px;top:282px;width:880px;text-align:center;font:400 16.5px/31px var(--sans);color:#fff}
.dots{position:absolute;left:0;width:1200px;top:372px;display:flex;justify-content:center;gap:4px}
.dots span{width:14px;height:14px;border-radius:50%;border:1.5px solid #ccc}
.dots span.on{background:#fff;border-color:#fff}

/* faq */
.faq{height:856px;background:#fff}
.faq .section-title{top:88px;font-size:31px;color:#111}
.faq-item{position:absolute;left:126px;width:946px;border:1.5px solid #d6d6d6;background:#fff}
.faq-item .q{position:absolute;left:36px;font:500 18px/34px var(--sans);color:#111;width:730px}
.faq-item .toggle{position:absolute;right:14px;width:56px;height:56px;font:700 30px var(--sans)}
.faq-item.open .q{font:400 24px var(--serif);color:var(--gold);top:24px;width:800px}
.faq-item.open .sep{position:absolute;left:36px;right:14px;top:82px;height:2px;background:#ddd}
.faq-item.open .a{position:absolute;left:40px;top:106px;width:870px;font:400 17px/34px var(--sans);color:#555}

/* footer */
.footer{height:627px;background:var(--ink)}
.footer .brand-mark{position:absolute;left:550px;top:100px;width:100px;height:100px;border-radius:50%;background:var(--gold)}
.footer .brand-name{left:0;width:1200px;top:222px;text-align:center;font:400 30px var(--serif);color:var(--gold)}
.footer-links{position:absolute;left:0;width:1200px;top:328px;display:flex;justify-content:center;gap:44px;font:400 13.5px var(--serif);color:#fff;text-transform:uppercase}
.contact{position:absolute;top:380px;display:flex;align-items:center;gap:26px;color:#fff;font:400 16px/26px var(--sans)}
.contact .ic{width:50px;height:50px;border-radius:3px;flex:none}
.socials{position:absolute;top:478px;left:0;width:1200px;display:flex;justify-content:center;gap:10px}
.socials span{width:34px;height:34px;border-radius:50%;background:var(--gold)}
.copy{position:absolute;top:556px;left:0;width:1200px;text-align:center;font:400 14px var(--sans);color:#fff}
</style>
</head>
<body>

<header>
  <div class="topbar">FREE SHIPPING ON ALL ORDERS</div>
  <nav class="nav" style="position:relative">
    <div class="brand"><span class="dot"></span><span class="name">PLOOIFRIS</span></div>
    <div class="nav-links">
      <a class="active" href="#">Home</a><a href="#">Benefits</a><a href="#">Product</a><a href="#">How It Works</a><a href="#">Customer Reviews</a><a href="#">FAQ</a>
    </div>
  </nav>
</header>

<section class="hero">
  <div class="hero-photo" role="img" aria-label="Photo of a hand placing a laundry strip into a washing machine drum"></div>
  <div class="abs kicker">Welcome To</div>
  <h1 class="abs">Sustainability Meets Luxury – Transform Your Laundry</h1>
  <div class="abs sub">Free shipping with no minimum order</div>
  <div class="abs cta gold-btn">Get Started</div>
</section>

<section class="benefits">
  <h2 class="section-title">PRODUCT BENEFITS</h2>
  <svg class="divider" style="top:122px" viewBox="0 0 142 22"><line x1="0" y1="11" x2="56" y2="11" stroke="#c8952a" stroke-width="2"/><line x1="86" y1="11" x2="142" y2="11" stroke="#c8952a" stroke-width="2"/><rect x="64" y="4" width="14" height="14" transform="rotate(45 71 11)" fill="none" stroke="#c8952a" stroke-width="2"/></svg>

  <div class="benefit" style="left:85px;top:190px">
    <div class="icon"><svg viewBox="0 0 160 160" width="160" height="160"><circle cx="80" cy="80" r="76" fill="#f7efe0"/><circle cx="80" cy="80" r="36" fill="#c8952a"/><path d="M66 74h28l-4 22H70z M72 74c0-8 16-8 16 0" fill="none" stroke="#fff" stroke-width="3"/></svg></div>
    <h3>ECO-FRIENDLINESS</h3>
    <p>Lorem ipsum dolor sit amet, consectetur adipiscing elit, sed do eiusmod tempor incididunt ut labore et dolore magna aliqua.</p>
  </div>
  <div class="benefit featured" style="left:441px;top:191px">
    <div class="icon"><svg viewBox="0 0 160 160" width="160" height="160"><circle cx="80" cy="80" r="76" fill="#e7c068"/><circle cx="80" cy="80" r="40" fill="#b8861e"/><path d="M80 60c-10 14-14 20-14 28a14 14 0 0 0 28 0c0-8-4-14-14-28z" fill="none" stroke="#fff" stroke-width="3"/></svg></div>
    <h3>LONG-LASTING SCENT</h3>
    <p>Lorem ipsum dolor sit amet, consectetur adipiscing elit, sed do eiusmod tempor aliqua.</p>
    <a class="more">Read More <svg width="16" height="16" viewBox="0 0 16 16"><circle cx="8" cy="8" r="7" fill="#c8952a"/><path d="M6 4l4 4-4 4" stroke="#fff" stroke-width="2" fill="none"/></svg></a>
  </div>
  <div class="benefit" style="left:797px;top:190px">
    <div class="icon"><svg viewBox="0 0 160 160" width="160" height="160"><circle cx="80" cy="80" r="76" fill="#f7efe0"/><circle cx="80" cy="80" r="36" fill="#c8952a"/><path d="M80 62l16 6v10c0 10-7 17-16 20-9-3-16-10-16-20V68z" fill="none" stroke="#fff" stroke-width="3"/></svg></div>
    <h3>HYPOALLERGENIC QUALITIES</h3>
    <p>Lorem ipsum dolor sit amet, consectetur adipiscing elit, sed do eiusmod tempor incididunt ut labore et dolore magna aliqua.</p>
  </div>
</section>

<section class="product">
  <div class="abs product-art" role="img" aria-label="Product box of Plooifris laundry strips"></div>
  <div class="abs eyebrow">OUR PRODUCT</div>
  <div class="abs rule"></div>
  <div class="abs pname">PLOOIFRIS</div>
  <div class="abs price">$45.00</div>
  <p class="abs desc">Lorem ipsum dolor sit amet, consectetur adipiscing elit, sed do eiusmod tempor incididunt ut labore et dolore magna aliqua. Ut nisi ut aliquip ex ea commodo consequat.</p>
  <div class="abs point" style="top:367px"><svg width="32" height="32" viewBox="0 0 32 32" style="flex:none;margin-top:6px"><rect x="9" y="9" width="14" height="14" transform="rotate(45 16 16)" fill="none" stroke="#c8952a" stroke-width="2"/><line x1="16" y1="2" x2="16" y2="30" stroke="#c8952a" stroke-width="1.5"/><line x1="2" y1="16" x2="30" y2="16" stroke="#c8952a" stroke-width="1.5"/></svg><span>Excepteur sint occaecat cupidatat non proident, sunt in culpa qui officia deserunt mollit anim id est laborum.</span></div>
  <div class="abs point" style="top:454px"><svg width="32" height="32" viewBox="0 0 32 32" style="flex:none"><rect x="9" y="9" width="14" height="14" transform="rotate(45 16 16)" fill="none" stroke="#c8952a" stroke-width="2"/><line x1="16" y1="2" x2="16" y2="30" stroke="#c8952a" stroke-width="1.5"/><line x1="2" y1="16" x2="30" y2="16" stroke="#c8952a" stroke-width="1.5"/></svg><span>Excepteur sint occaecat cupidatat anim id est laborum.</span></div>
  <div class="abs cta gold-btn">Try Now – Free Shipping</div>
</section>

<section class="how">
  <h2 class="section-title">How It Works</h2>
  <svg class="divider" style="top:136px" viewBox="0 0 142 22"><line x1="0" y1="11" x2="56" y2="11" stroke="#c8952a" stroke-width="2"/><line x1="86" y1="11" x2="142" y2="11" stroke="#c8952a" stroke-width="2"/><rect x="64" y="4" width="14" height="14" transform="rotate(45 71 11)" fill="none" stroke="#c8952a" stroke-width="2"/></svg>
  <p class="intro">Lorem ipsum dolor sit amet, consectetur adipiscing elit, sed do eiusmod tempor incididunt ut labore et dolore magna aliqua. Ut enim ad minim veniam, quis nostrud exercitation ullamco laboris nisi ut aliquip ex ea commodo consequat.</p>

  <svg class="abs" style="left:0;top:0" width="1200" height="761" viewBox="0 0 1200 761">
    <g fill="none" stroke="#444" stroke-width="1.2" stroke-dasharray="4 4">
      <path d="M276 328L352 302V590H592V302H830V590L910 562"/>
    </g>
    <circle cx="276" cy="328" r="5" fill="#c8952a"/><circle cx="910" cy="562" r="5" fill="#c8952a"/>
  </svg>

  <div class="step" style="left:100px;top:359px">
    <div class="diamond"><span class="sq"></span><div class="badge">STEP<span>01</span></div></div>
    <h3>Tear a Strip</h3>
    <p>Excepteur sint occaecat cupidatat non proident, sunt in culpa qui officia deserunt mollit anim id est laborum.</p>
  </div>
  <div class="step" style="left:358px;top:274px">
    <div class="diamond"><span class="sq"></span><div class="badge">STEP<span>02</span></div></div>
    <h3>Place It in the Drum</h3>
    <p>Excepteur sint occaecat cupidatat non proident, sunt in culpa qui officia deserunt mollit anim id est laborum.</p>
  </div>
  <div class="step" style="left:600px;top:359px">
    <div class="diamond"><span class="sq"></span><div class="badge">STEP<span>03</span></div></div>
    <h3>Add Clothes</h3>
    <p>Excepteur sint occaecat cupidatat non proident, sunt in culpa qui officia deserunt mollit anim id est laborum.</p>
  </div>
  <div class="step" style="left:850px;top:274px">
    <div class="diamond"><span class="sq"></span><div class="badge">STEP<span>04</span></div></div>
    <h3>Set Washing Cycle</h3>
    <p>Excepteur sint occaecat cupidatat non proident, sunt in anim id est laborum.</p>
  </div>
</section>

<section class="testimonials">
  <h2 class="section-title">Testimonials</h2>
  <svg class="divider" style="top:132px" viewBox="0 0 142 22"><line x1="0" y1="11" x2="56" y2="11" stroke="#c8952a" stroke-width="2"/><line x1="86" y1="11" x2="142" y2="11" stroke="#c8952a" stroke-width="2"/><rect x="64" y="4" width="14" height="14" transform="rotate(45 71 11)" fill="none" stroke="#c8952a" stroke-width="2"/></svg>
  <div class="quote-mark">“</div>
  <blockquote>"Sed ut perspiciatis unde omnis iste natus error sit voluptatem accusantium doloremque laudantium, totam rem aperiam, eaque ipsa quae ab illo inventore veritatis et quasi architecto beatae vitae dicta sunt explicabo."</blockquote>
  <div class="dots"><span></span><span></span><span class="on"></span><span></span><span></span></div>
</section>

<section class="faq">
  <h2 class="section-title">FAQ</h2>
  <svg class="divider" style="top:140px" viewBox="0 0 142 22"><line x1="0" y1="11" x2="56" y2="11" stroke="#c8952a" stroke-width="2"/><line x1="86" y1="11" x2="142" y2="11" stroke="#c8952a" stroke-width="2"/><rect x="64" y="4" width="14" height="14" transform="rotate(45 71 11)" fill="none" stroke="#c8952a" stroke-width="2"/></svg>

  <div class="faq-item open" style="top:190px;height:234px">
    <div class="q">Lorem ipsum dolor sit amet, consectetur adipiscing elit?</div>
    <div class="toggle gold-btn" style="top:12px">-</div>
    <div class="sep"></div>
    <p class="a">Lorem ipsum dolor sit amet, consectetur adipiscing elit, sed do eiusmod tempor incididunt ut labore et dolore magna aliqua. Ut enim ad minim veniam, quis nostrud exercitation ullamco laboris nisi ut aliquip ex ea commodo consequat.</p>
  </div>
  <div class="faq-item" style="top:459px;height:80px">
    <div class="q" style="top:5px">Lorem ipsum dolor sit amet, consectetur adipiscing elit, sed do eiusmod tempor incididunt ut labore</div>
    <div class="toggle gold-btn" style="top:11px">+</div>
  </div>
  <div class="faq-item" style="top:566px;height:80px">
    <div class="q" style="top:5px">Lorem ipsum dolor sit amet, consectetur adipiscing elit, sed do eiusmod tempor incididunt ut labore</div>
    <div class="toggle gold-btn" style="top:11px">+</div>
  </div>
  <div class="faq-item" style="top:674px;height:80px">
    <div class="q" style="top:5px">Lorem ipsum dolor sit amet, consectetur adipiscing elit, sed do eiusmod tempor incididunt ut labore</div>
    <div class="toggle gold-btn" style="top:11px">+</div>
  </div>
</section>

<footer class="footer">
  <div class="brand-mark"></div>
  <div class="abs brand-name">PLOOIFRIS</div>
  <div class="footer-links"><span>Home</span><span>Benefits</span><span>Product</span><span>How It Works</span><span>Customer Reviews</span><span>FAQ</span></div>
  <div class="contact" style="left:152px"><svg class="ic" viewBox="0 0 50 50"><rect width="50" height="50" rx="3" fill="#c8952a"/><rect x="14" y="17" width="22" height="16" fill="#fff"/><path d="M14 17l11 9 11-9" fill="none" stroke="#c8952a" stroke-width="2"/></svg><span>info@plooifris.nl</span></div>
  <div class="contact" style="left:458px"><svg class="ic" viewBox="0 0 50 50"><rect width="50" height="50" rx="3" fill="#c8952a"/><path d="M25 13a8 8 0 0 0-8 8c0 6 8 15 8 15s8-9 8-15a8 8 0 0 0-8-8z" fill="#fff"/><circle cx="25" cy="21" r="3" fill="#c8952a"/></svg><span>48 Linden Lane, Suite 12,<br>Harbor Vale, FL 33100</span></div>
  <div class="contact" style="left:868px"><svg class="ic" viewBox="0 0 50 50"><rect width="50" height="50" rx="3" fill="#c8952a"/><path d="M17 15l5 0 2 6-3 2a14 14 0 0 0 6 6l2-3 6 2 0 5c-10 1-19-8-18-18z" fill="#fff"/></svg><span>0201 555 874</span></div>
  <div class="socials"><span></span><span></span><span></span><span></span></div>
  <div class="copy">Copyrights@2024.Plooifris.All Rights Reserved</div>
</footer>

</body>
</html>
```